Commercial Construction Company

We need a business card design based on our current logo. We are a commercial general contractor based in Southern California that specializes in bank remodels. We would like to see designs that incorporate dark blue. The final design should portray an image of professionalism and quality.

If possible, I would like to add metallic foil to the design. Thank you

```html
<!DOCTYPE html>
<html lang="en">
<head>
<meta charset="utf-8">
<title>Harlow Builders – Business Card</title>
<link href="https://fonts.googleapis.com/css2?family=Arimo:wght@400;700&display=swap" rel="stylesheet">
<style>
  :root {
    --navy: #243456;
    --royal: #164a80;
    --steel: #9d9d9d;
    --ink-blue: #1f47a8;
    --paper: #ffffff;
    --backdrop-light: #ebeaea;
    --backdrop-dark: #a9a8a8;
  }
  * { margin: 0; padding: 0; box-sizing: border-box; }
  html, body { width: 1200px; height: 807px; overflow: hidden; }
  body {
    background: linear-gradient(135deg, var(--backdrop-light) 0%, #d6d5d5 55%, var(--backdrop-dark) 100%);
    font-family: "Arimo", Arial, sans-serif;
    position: relative;
  }
  .card {
    position: absolute;
    left: 340px;
    width: 520px;
    height: 297px;
    box-shadow: 0 6px 18px rgba(0,0,0,0.25);
    overflow: hidden;
  }
  .card--front { top: 70px; background: var(--paper); }
  .card--back { top: 440px; background: var(--navy); }
  .card svg.shapes { position: absolute; inset: 0; }

  .brand {
    position: absolute;
    display: flex;
    align-items: center;
    gap: 8px;
    font-weight: 700;
  }
  .brand__dot { width: 18px; height: 18px; border-radius: 50%; }
  .brand--front { top: 28px; right: 120px; color: var(--navy); font-size: 22px; }
  .brand--front .brand__dot { background: var(--royal); }
  .brand--back {
    top: 50%; left: 50%; transform: translate(-50%, -50%);
    color: var(--paper); font-size: 34px; letter-spacing: 2px; gap: 14px;
  }
  .brand--back .brand__dot { width: 28px; height: 28px; background: var(--paper); }

  .contact { position: absolute; left: 34px; bottom: 28px; color: var(--ink-blue); }
  .contact__name { font-size: 22px; font-weight: 700; letter-spacing: 0.5px; }
  .contact__role { font-size: 17px; margin-top: 2px; }
  .contact__rule { width: 165px; height: 2px; background: var(--navy); margin: 10px 0 12px; }
  .contact__list { list-style: none; font-size: 16px; }
  .contact__list li { display: flex; align-items: center; gap: 10px; line-height: 25px; }
  .contact__icon {
    width: 14px; height: 14px; background: var(--royal); border-radius: 2px;
    display: inline-flex; align-items: center; justify-content: center;
  }
</style>
</head>
<body>

<section class="card card--front" aria-label="Card front">
  <svg class="shapes" width="520" height="297" viewBox="0 0 520 297">
    <polygon points="395,58 520,58 520,150 455,150" fill="var(--steel)"/>
    <polygon points="380,170 520,170 520,240 345,240" fill="var(--royal)"/>
    <polygon points="300,252 520,252 520,297 280,297" fill="var(--navy)"/>
  </svg>
  <div class="brand brand--front"><span class="brand__dot"></span>HB</div>
  <div class="contact">
    <p class="contact__name">Dana Reyes</p>
    <p class="contact__role">Founder &amp; CEO</p>
    <div class="contact__rule"></div>
    <ul class="contact__list">
      <li><span class="contact__icon"><svg width="10" height="10" viewBox="0 0 10 10"><path d="M2 1 L4 1 L4.5 3 L3.5 4 Q4.5 6 6 6.5 L7 5.5 L9 6 L9 8 Q5 9 2 5 Q1 3 2 1Z" fill="#fff"/></svg></span>+0012 3344 5566</li>
      <li><span class="contact__icon"><svg width="10" height="10" viewBox="0 0 10 10"><rect x="1" y="2.5" width="8" height="5.5" fill="none" stroke="#fff"/><path d="M1 2.5 L5 6 L9 2.5" fill="none" stroke="#fff"/></svg></span>hello@harlowbuild.com</li>
      <li><span class="contact__icon"><svg width="10" height="10" viewBox="0 0 10 10"><circle cx="5" cy="5" r="3.8" fill="none" stroke="#fff"/><path d="M1.2 5 H8.8 M5 1.2 V8.8" stroke="#fff" stroke-width="0.8"/></svg></span>www.harlowbuild.com</li>
    </ul>
  </div>
</section>

<section class="card card--back" aria-label="Card back">
  <svg class="shapes" width="520" height="297" viewBox="0 0 520 297">
    <polygon points="0,0 60,0 0,45" fill="var(--paper)"/>
    <polygon points="0,45 60,0 120,0 0,110" fill="var(--steel)"/>
    <polygon points="520,297 470,297 520,255" fill="var(--paper)"/>
    <polygon points="400,297 470,297 520,255 520,210" fill="var(--steel)"/>
    <polygon points="520,0 430,0 520,80" fill="var(--royal)"/>
  </svg>
  <div class="brand brand--back"><span class="brand__dot"></span>HARLOW BUILDERS</div>
</section>

</body>
</html>
```